Create Lanternfield HR Business Cards.

Create Business Cards for Lanternfield HR. 2 sided and Would like the back to have the logo.

Info for Business Card:
Address: 4827 Millbrook Ave Suite 230 Cleveland, Ohio 44987
Office Number: 216-555-0143
Mobile: 216-555-0192

Website: www.lanternfieldhr.example

Target Market(s)

Small to medium size businesses

Industry/Entity Type

Human Resources

Contact Information for Business Card

Company logo and information

Font styles to use
Serif
Sans Serif

Requirements
Must have
• Info for Business Card: Address: 4827 Millbrook Ave Suite 230 Cleveland, Ohio 44987 Office Number: 216-555-0143 Mobile: 216-555-0192 Website: www.lanternfieldhr.example

```html
<!DOCTYPE html>
<html lang="en">
<head>
<meta charset="utf-8">
<title>Lanternfield HR Business Cards</title>
<link rel="stylesheet" href="https://fonts.googleapis.com/css2?family=Outfit:wght@400;500;600&display=swap">
<style>
  :root {
    --navy: #27215f;
    --orange: #f0821e;
    --paper: #ffffff;
    --ink-soft: #4a4a55;
    --backdrop: #2b2b2d;
  }
  * { box-sizing: border-box; margin: 0; padding: 0; }
  html, body {
    width: 1200px; height: 900px; overflow: hidden;
    background: var(--backdrop);
    font-family: "Outfit", sans-serif;
  }
  .stage { position: relative; width: 1200px; height: 900px; }
  .card {
    position: absolute;
    width: 580px; height: 330px;
    background: var(--paper);
    overflow: hidden;
    box-shadow: 0 10px 30px rgba(0,0,0,.45);
  }
  .card--front { left: 60px; top: 70px; }
  .card--back { left: 560px; top: 490px; }

  .brand {
    position: absolute;
    display: flex; align-items: center; gap: 12px;
  }
  .brand__dot {
    width: 34px; height: 34px; border-radius: 50%;
    background: var(--orange); flex: none;
  }
  .brand__name {
    color: var(--navy);
    font-weight: 600;
    font-size: 34px;
    letter-spacing: .5px;
    line-height: 1;
  }
  .card--front .brand { right: 40px; top: 110px; }
  .card--back .brand { right: 36px; top: 70px; }
  .card--back .brand__name { font-size: 30px; }
  .card--back .brand__dot { width: 30px; height: 30px; }

  .card__bands { position: absolute; left: 0; bottom: 0; width: 580px; display: block; }

  .website {
    position: absolute;
    color: var(--navy);
    font-weight: 500;
    font-size: 17px;
    letter-spacing: .3px;
  }
  .card--front .website { left: 26px; bottom: 26px; }
  .card--back .website { right: 22px; bottom: 38px; }

  .contact {
    position: absolute; left: 60px; top: 118px;
    color: var(--ink-soft);
    font-size: 16px; line-height: 1.35;
  }
  .contact__line { display: flex; align-items: center; gap: 10px; }
  .contact__icon { width: 14px; height: 16px; flex: none; }
  .contact__address { margin-top: 16px; padding-left: 24px; }
</style>
</head>
<body>
<main class="stage">

  <section class="card card--front" aria-label="Card front">
    <div class="brand">
      <span class="brand__dot"></span>
      <span class="brand__name">Lanternfield HR</span>
    </div>
    <svg class="card__bands" viewBox="0 0 580 72" height="72" aria-hidden="true">
      <rect x="0" y="50" width="580" height="22" fill="var(--navy)"/>
      <path d="M0 72 V12 H205 Q228 12 244 24 L290 50 V72 Z" fill="var(--orange)"/>
    </svg>
    <span class="website">www.lanternfieldhr.example</span>
  </section>

  <section class="card card--back" aria-label="Card back">
    <div class="brand">
      <span class="brand__dot"></span>
      <span class="brand__name">Lanternfield HR</span>
    </div>

    <div class="contact">
      <p class="contact__line">
        <svg class="contact__icon" viewBox="0 0 14 16" aria-label="Mobile"><rect x="2.5" y="0.75" width="9" height="14.5" rx="1.5" fill="none" stroke="var(--navy)" stroke-width="1.5"/><line x1="6" y1="12.5" x2="8" y2="12.5" stroke="var(--navy)" stroke-width="1.5"/></svg>
        <span>216-555-0192</span>
      </p>
      <p class="contact__line">
        <svg class="contact__icon" viewBox="0 0 16 16" aria-label="Office"><path d="M3 1.5 L6 1.5 L7 5 L5.2 6.4 Q6.5 9.5 9.6 10.8 L11 9 L14.5 10 L14.5 13 Q14.5 14.5 13 14.5 Q2 14 1.5 3 Q1.5 1.5 3 1.5 Z" fill="var(--navy)"/></svg>
        <span>216-555-0143</span>
      </p>
      <p class="contact__address">4827 Millbrook Ave<br>Suite 230 Cleveland, Ohio 44987</p>
    </div>

    <svg class="card__bands" viewBox="0 0 580 92" height="92" aria-hidden="true">
      <rect x="0" y="70" width="400" height="22" fill="var(--navy)"/>
      <path d="M375 92 V30 Q375 0 405 0 H580 V92 Z" fill="var(--orange)"/>
    </svg>
    <span class="website">www.lanternfieldhr.example</span>
  </section>

</main>
</body>
</html>
```